TBranwell executive consulting

We need a basic clean website for executive consulting. Rosalind is the previos CIO for bluecrest airways and currently supports several technology companies with innovation and transformation.

Target Market(s)

C level technology and CIO training

Industry/Entity Type

Technology and travel industry

Coding

Coded - Design and coding required

Number of Pages Required

3 page

Font styles to use
Sans Serif

Colors
0054AA
0677BA
7BADD7
CADEEF
E8F1F8
0094D4
00A9DD
6FCCEA
C7EBF8
E9F6FB

Requirements
Must have
• Home page, about us, services social media links

```html
<!DOCTYPE html>
<html lang="en">
<head>
<meta charset="utf-8">
<title>TBranwell Executive Consulting</title>
<link href="https://fonts.googleapis.com/css2?family=Roboto:ital,wght@0,400;0,500;0,700;1,400&display=swap" rel="stylesheet">
<style>
:root{
  --navy:#2d3a5f;
  --navy-deep:#1c2a55;
  --blue-dark:#0054aa;
  --blue:#0677ba;
  --cyan:#00a9dd;
  --cyan-mid:#0094d4;
  --sky:#6fccea;
  --pale:#e9f6fb;
  --grey-bg:#f3f4f6;
  --ink:#1e1e1e;
  --text:#333;
  --white:#fff;
}
*{margin:0;padding:0;box-sizing:border-box}
html,body{width:1200px;height:4732px;overflow:hidden}
body{position:relative;font-family:'Roboto',sans-serif;color:var(--text);background:var(--white)}
.abs{position:absolute}
a{color:inherit;text-decoration:none}

.topbar{left:0;top:0;width:1200px;height:42px;background:var(--navy);color:var(--white);font-size:15px;z-index:3}
.topbar .call{position:absolute;right:128px;top:12px;display:flex;align-items:center;gap:8px}
.nav{left:0;top:42px;width:1200px;height:90px;background:var(--white);z-index:3}
.brand{position:absolute;left:127px;top:28px;font-size:28px;font-weight:700;color:var(--navy);display:flex;align-items:center;gap:10px}
.brand .dot{width:14px;height:14px;border-radius:50%;background:var(--cyan)}
.menu{position:absolute;right:128px;top:36px;display:flex;gap:50px;font-size:15px;font-weight:500;color:var(--ink)}
.menu .active{color:var(--cyan)}

.hero{left:0;top:132px;width:1200px;height:640px;clip-path:polygon(0 0,100% 0,100% 85.6%,0 100%);
  background:radial-gradient(circle at 68% 40%,#1c6fb6 0%,#0d3b7a 30%,#0a1f4a 65%,#081634 100%)}
.hero-art{position:absolute;left:560px;top:0;width:640px;height:560px}
.hero-title{position:absolute;left:124px;top:90px;color:var(--white);font-size:86px;font-weight:700;line-height:1;letter-spacing:-1px}
.hero-sub{position:absolute;left:124px;top:168px;color:var(--white);font-size:42px;font-weight:500}
.btn{display:inline-block;background:var(--cyan);color:var(--white);font-weight:700;font-size:18px;border-radius:30px;text-align:center}
.hero .btn{position:absolute;left:127px;top:244px;width:197px;height:58px;line-height:58px}

.deco{left:0;top:680px;width:1200px;height:900px;pointer-events:none}

.about-label{left:124px;top:880px;font-size:28px;color:#c4c4c4;font-weight:500}
.about-name{left:124px;top:918px;font-size:54px;color:var(--ink);font-weight:500}
.about-text{left:124px;top:993px;width:432px;font-size:14px;line-height:21.5px;color:var(--ink)}
.about-btn{left:128px;top:1222px;width:198px;height:56px;line-height:56px}
.portrait{left:638px;top:829px;width:434px;height:527px;border-radius:22px;
  background:linear-gradient(160deg,#c9c3b8 0%,#8b8a86 45%,#2a2c35 100%)}

.services-bg{left:0;top:1516px;width:1200px;height:1110px;background:var(--grey-bg)}
.services-edge{left:0;top:1516px;width:1200px;height:70px}
.section-title{width:1200px;left:0;text-align:center;font-weight:500;color:var(--ink)}
.services-title{top:1665px;font-size:64px}
.svc{top:1786px;width:150px;text-align:center;font-size:15px;font-weight:500;line-height:20px;color:var(--ink)}
.svc .ring{width:114px;height:114px;border-radius:50%;background:var(--cyan);margin:0 auto 34px;display:flex;align-items:center;justify-content:center}
.svc.active .ring{background:linear-gradient(180deg,var(--cyan),var(--navy))}
.detail-photo{left:127px;top:2093px;width:474px;height:370px;border-radius:18px;
  background:linear-gradient(135deg,#1f2c4e 0%,#3b4f78 50%,#c9ccd6 100%)}
.detail-title{left:636px;top:2118px;width:460px;font-size:34px;font-weight:500;line-height:34px;color:var(--ink)}
.detail-list{left:636px;top:2218px;width:450px;list-style:none;font-size:18px;line-height:26px;color:var(--ink)}
.detail-list li{position:relative;padding-left:28px;margin-bottom:24px}
.detail-list li::before{content:"";position:absolute;left:2px;top:9px;width:9px;height:9px;border-radius:50%;background:var(--cyan)}

.testi{left:0;top:2570px;width:1200px;height:771px;
  clip-path:polygon(0 0,24% 5.8%,100% 5.8%,100% 100%,0 83.8%);
  background:linear-gradient(135deg,#1a5e98 0%,#1c3f7a 45%,#1b2a62 100%)}
.testi-band{left:400px;top:2614px;width:800px;height:76px;background:var(--cyan);clip-path:polygon(0 0,100% 0,100% 100%)}
.testi-title{top:2730px;font-size:46px;color:var(--white)}
.quote{left:230px;top:2846px;width:790px;text-align:center;font-style:italic;font-size:17px;line-height:24px;color:var(--white)}
.quote p{margin-bottom:24px}
.qmark{font-size:90px;font-weight:700;color:var(--white);line-height:1}
.author{top:3124px;font-size:16px;font-weight:700;color:var(--white);text-align:center;width:1200px;left:0}

.expertise-title{top:3380px;font-size:62px}
.card{top:3503px;width:204px;height:259px;background:var(--white);border-radius:16px;box-shadow:0 4px 22px rgba(0,0,0,.09);text-align:center;padding-top:24px;font-size:22px;font-weight:500;line-height:27px;color:var(--ink)}
.card svg{display:block;margin:0 auto 22px}

.consult-band{left:0;top:3841px;width:1200px;height:511px;background:var(--grey-bg);clip-path:polygon(0 0,100% 9%,100% 100%,0 100%)}
.consult-photo{left:600px;top:3930px;width:600px;height:422px;
  background:linear-gradient(90deg,rgba(243,244,246,1) 0%,#b9c4cf 25%,#6e8aa3 60%,#2f4a6e 100%)}
.consult-title{left:126px;top:4008px;width:560px;font-size:40px;line-height:46px;font-weight:500;color:var(--navy)}
.consult-text{left:126px;top:4130px;width:580px;font-size:14px;line-height:21px;color:var(--ink)}
.consult-btn{left:129px;top:4227px;width:198px;height:56px;line-height:56px}

.footer-band{left:0;top:4300px;width:1200px;height:432px;background:var(--navy);clip-path:polygon(0 35%,100% 0,100% 100%,0 100%)}
.foot-brand{left:151px;top:4458px;font-size:30px;font-weight:700;color:var(--white);display:flex;align-items:center;gap:10px}
.foot-brand .dot{width:14px;height:14px;border-radius:50%;background:var(--cyan)}
.foot-h{top:4418px;font-size:27px;font-weight:500;color:var(--white)}
.foot-h::after{content:"";display:block;width:66px;height:2px;background:var(--white);margin-top:14px}
.foot-links{left:384px;top:4497px;list-style:none;font-size:14px;line-height:23px;color:var(--white)}
.foot-contact{left:575px;top:4497px;width:240px;list-style:none;font-size:14px;line-height:18px;color:var(--white)}
.foot-contact li{display:flex;gap:10px;margin-bottom:16px}
.social{left:904px;top:4496px;display:flex;gap:8px}
.social span{width:33px;height:33px;border-radius:50%;border:1.5px solid var(--white)}
.copy{left:0;top:4688px;width:1200px;text-align:center;font-size:14px;color:var(--white)}
</style>
</head>
<body>

<header>
  <div class="abs topbar"><div class="call">
    <svg width="15" height="15" viewBox="0 0 24 24"><path fill="#fff" d="M6.6 10.8a15.1 15.1 0 0 0 6.6 6.6l2.2-2.2c.3-.3.7-.4 1-.2 1.1.4 2.3.6 3.6.6.6 0 1 .4 1 1V20c0 .6-.4 1-1 1C10.6 21 3 13.4 3 4c0-.6.4-1 1-1h3.5c.6 0 1 .4 1 1 0 1.3.2 2.5.6 3.6.1.3 0 .7-.2 1z"/></svg>
    Call Us: 123 4567 899</div></div>
  <nav class="abs nav">
    <a class="brand" href="#"><span class="dot"></span>TBranwell</a>
    <div class="menu"><a class="active" href="#">HOME</a><a href="#">OUR SERVICES</a><a href="#">ABOUT US</a><a href="#">TESTIMONIALS</a><a href="#">CONTACT</a></div>
  </nav>
</header>

<div class="abs hero">
  <div class="hero-art" role="img" aria-label="Glowing low-poly butterflies emerging from a chrysalis over a blue network of points"
       style="background:radial-gradient(ellipse at 50% 35%,rgba(110,204,234,.55) 0%,rgba(0,148,212,.25) 35%,rgba(0,0,0,0) 70%)"></div>
  <h1 class="hero-title">TBranwell</h1>
  <h2 class="hero-sub">Executive Consulting</h2>
  <a class="btn" href="#">CONTACT US</a>
</div>

<svg class="abs deco" viewBox="0 680 1200 900" width="1200" height="900" aria-hidden="true">
  <path d="M1000 705 C980 760 990 830 1040 870 C1090 910 1150 1080 1200 1110" fill="none" stroke="#00a9dd" stroke-width="3"/>
  <path d="M0 1283 C80 1290 130 1360 130 1420 C130 1460 118 1495 105 1516" fill="none" stroke="#00a9dd" stroke-width="3"/>
</svg>

<div class="abs about-label">About Us</div>
<h2 class="abs about-name">Rosalind Branwell</h2>
<p class="abs about-text">Rosalind Branwell is a seasoned leader with a remarkable 40-year career in the travel industry, including 20 transformative years at Bluecrest Airways. As the Senior Vice President of Technology (CIO), Rosalind spearheaded some of the company's most significant technological and strategic transformations, helping Bluecrest Airways stay at the forefront of innovation in the competitive travel market. Her work bridged the gap between business strategy and technology, driving measurable success and resilience.</p>
<a class="abs btn about-btn" href="#">READ MORE</a>
<div class="abs portrait" role="img" aria-label="Portrait photograph of Rosalind Branwell in a dark blazer"></div>

<div class="abs services-bg"></div>
<svg class="abs services-edge" viewBox="0 0 1200 70" width="1200" height="70" aria-hidden="true">
  <polygon points="0,0 550,0 0,66" fill="#2d3a5f"/>
</svg>
<h2 class="abs section-title services-title">Services Offered</h2>

<div class="abs svc" style="left:59px"><div class="ring"><svg width="62" height="62" viewBox="0 0 60 60" fill="none" stroke="#fff" stroke-width="2"><circle cx="30" cy="14" r="7"/><path d="M27 22h6"/><circle cx="17" cy="34" r="5"/><circle cx="43" cy="34" r="5"/><circle cx="30" cy="32" r="5"/><path d="M8 52c0-8 5-12 9-12s9 4 9 12M34 52c0-8 5-12 9-12s9 4 9 12M22 50c0-7 4-11 8-11s8 4 8 11"/></svg></div>Leadership<br>Mentorship</div>
<div class="abs svc" style="left:210px"><div class="ring"><svg width="62" height="62" viewBox="0 0 60 60" fill="none" stroke="#fff" stroke-width="2"><rect x="10" y="10" width="40" height="28"/><path d="M16 20l4 4 6-8M34 18l6 6M40 18l-6 6M18 32h24M20 38l-6 14M40 38l6 14M30 38v8"/></svg></div>Technology<br>Strategy<br>Development</div>
<div class="abs svc" style="left:366px"><div class="ring"><svg width="62" height="62" viewBox="0 0 60 60" fill="none" stroke="#fff" stroke-width="2"><path d="M14 24a8 8 0 1 1 12 0v6h-12z"/><circle cx="42" cy="20" r="6"/><circle cx="42" cy="20" r="2"/><path d="M20 30v22M36 52V36l6-6 6 6v16M12 52h40"/></svg></div>Digital<br>Transformation<br>Consulting</div>
<div class="abs svc active" style="left:521px"><div class="ring"><svg width="62" height="62" viewBox="0 0 60 60" fill="none" stroke="#fff" stroke-width="2"><circle cx="30" cy="24" r="9"/><circle cx="30" cy="24" r="3"/><path d="M30 11v-4M30 41v-4M17 24h-4M47 24h-4"/><circle cx="14" cy="44" r="4"/><circle cx="30" cy="44" r="4"/><circle cx="46" cy="44" r="4"/><path d="M8 56c0-4 3-6 6-6s6 2 6 6M24 56c0-4 3-6 6-6s6 2 6 6M40 56c0-4 3-6 6-6s6 2 6 6"/></svg></div>IT-Business<br>Partnership<br>Development</div>
<div class="abs svc" style="left:673px"><div class="ring"><svg width="62" height="62" viewBox="0 0 60 60" fill="none" stroke="#fff" stroke-width="2"><rect x="8" y="10" width="14" height="10" rx="2"/><rect x="38" y="10" width="14" height="10" rx="2"/><circle cx="20" cy="30" r="4"/><circle cx="40" cy="30" r="4"/><path d="M12 52V40l8-4 8 6M48 52V40l-8-4-8 6M26 46h8"/></svg></div>Organizational<br>Change<br>Management</div>
<div class="abs svc" style="left:825px"><div class="ring"><svg width="62" height="62" viewBox="0 0 60 60" fill="none" stroke="#fff" stroke-width="2"><path d="M10 52h40M14 52V42M22 52V36M30 52V30M10 38l12-10 8 4 14-16"/><path d="M38 16h6v6"/><circle cx="46" cy="34" r="4"/><path d="M42 52V42h8v10"/></svg></div>Program<br>and Project<br>Oversight</div>
<div class="abs svc" style="left:976px"><div class="ring"><svg width="62" height="62" viewBox="0 0 60 60" fill="none" stroke="#fff" stroke-width="2"><circle cx="30" cy="18" r="8"/><circle cx="30" cy="18" r="3"/><path d="M8 38l10-6 8 4h10l-12 8M52 38l-10-6-8 4M14 50l10-8M46 50l-12-12"/></svg></div>Advisory Services<br>for CIOs and IT<br>Executives</div>

<div class="abs detail-photo" role="img" aria-label="Photo of business people passing a clipboard across a table"></div>
<h3 class="abs detail-title">IT-Business Partnership Development</h3>
<ul class="abs detail-list">
  <li>Workshops and training sessions to strengthen collaboration between IT and business units.</li>
  <li>Building governance frameworks for seamless communication and decision-making.</li>
  <li>Helping organizations adopt a value-driven approach to IT investments</li>
</ul>

<div class="abs testi"></div>
<div class="abs testi-band"></div>
<h2 class="abs section-title testi-title">Testimonials</h2>
<div class="abs qmark" style="left:152px;top:2818px">&ldquo;</div>
<div class="abs quote">
  <p>Rosalind is a decisive and fair leader who exemplifies strength, wisdom, and empathy. She always possesses a clear vision for the future and is willing to make bold decisions which are grounded in data, expertise, and intuition while remaining open to diverse perspectives.</p>
  <p>Rosalind's leadership style fosters an inclusive environment where every voice matters, empowering her team to excel and innovate. She was able to balance ambition with humanity and succeeded in prioritizing the well-being of her people, ensuring they feel valued and supported.</p>
  <p>In times of uncertainty her unwavering confidence and fairness inspire trust, driving the organization forward with resilience and integrity</p>
</div>
<div class="abs qmark" style="left:1024px;top:3050px">&rdquo;</div>
<div class="abs author">MARTIN OAKES, CEO VELTRIX</div>

<h2 class="abs section-title expertise-title">Expertise</h2>
<div class="abs card" style="left:127px"><svg width="86" height="86" viewBox="0 0 60 60" fill="none" stroke="#00a9dd" stroke-width="1.6"><path d="M50 10c-3-3-7 0-9 2L33 20 14 15l-4 4 15 9-7 7-6-1-3 3 7 4 4 7 3-3-1-6 7-7 9 15 4-4-5-19 8-8c2-2 5-6 2-9z"/><path d="M8 52l6-2M46 46l4 4"/></svg>Airline<br>Expertise</div>
<div class="abs card" style="left:375px"><svg width="86" height="86" viewBox="0 0 60 60" fill="none" stroke="#00a9dd" stroke-width="1.6"><path d="M8 24h10a4 4 0 1 1 6 0h10v10a4 4 0 1 0 0 6v10H8z"/><path d="M20 24v10a4 4 0 1 1 0 6"/><path d="M34 14l8-8 6 6a4 4 0 1 1 4 4l6 6-8 8"/></svg>Enterprise<br>wide strategic<br>initiatives</div>
<div class="abs card" style="left:623px"><svg width="86" height="86" viewBox="0 0 60 60" fill="none" stroke="#00a9dd" stroke-width="1.6"><path d="M28 8c10 0 18 8 18 18l4 8h-4v8c0 3-2 5-5 5h-5v7M18 56V44c-4-4-7-10-7-16 0-11 8-20 17-20"/><circle cx="28" cy="24" r="6"/><path d="M26 32h4M26 35h4M28 14v-3M18 24h-3M38 24h3M21 17l-2-2M35 17l2-2"/></svg>Technology<br>Products and<br>services</div>
<div class="abs card" style="left:869px"><svg width="86" height="86" viewBox="0 0 60 60" fill="none" stroke="#00a9dd" stroke-width="1.6"><circle cx="42" cy="18" r="10"/><circle cx="42" cy="18" r="5"/><circle cx="42" cy="18" r="1.5"/><path d="M30 18H16a7 7 0 0 0 0 14h24a7 7 0 0 1 0 14H18"/><path d="M8 46l10-5v10z"/></svg>Strategy<br>and Change<br>leadership</div>

<div class="abs consult-band"></div>
<div class="abs consult-photo" role="img" aria-label="Photo of two smiling colleagues in conversation in a bright office"></div>
<h2 class="abs consult-title">Comprehensive Consulting, Flexible Scheduling</h2>
<p class="abs consult-text">Lorem ipsum dolor sit amet, consectetur adipiscing elit, sed do eiusmod tempor incididunt ut labore et dolore magna alia. Quis ipsum suspendisse ultr ices gravida. Risus commodo viverra maecenas accumsan lacus vel facilisis.</p>
<a class="abs btn consult-btn" href="#">CONTACT US</a>

<footer>
  <div class="abs footer-band"></div>
  <div class="abs foot-brand"><span class="dot"></span>TBranwell</div>
  <h4 class="abs foot-h" style="left:384px">Links</h4>
  <ul class="abs foot-links"><li>Home</li><li>About us</li><li>Services</li><li>Contact</li><li>Blog</li></ul>
  <h4 class="abs foot-h" style="left:575px">Contact</h4>
  <ul class="abs foot-contact">
    <li><svg width="14" height="16" viewBox="0 0 24 24"><path fill="#fff" d="M12 2a7 7 0 0 0-7 7c0 5 7 13 7 13s7-8 7-13a7 7 0 0 0-7-7zm0 9.5A2.5 2.5 0 1 1 12 6.5a2.5 2.5 0 0 1 0 5z"/></svg><span>Lorem Dum street 123 LJD<br>dumy numers 463.</span></li>
    <li><svg width="14" height="14" viewBox="0 0 24 24"><path fill="#fff" d="M6.6 10.8a15.1 15.1 0 0 0 6.6 6.6l2.2-2.2c.3-.3.7-.4 1-.2 1.1.4 2.3.6 3.6.6.6 0 1 .4 1 1V20c0 .6-.4 1-1 1C10.6 21 3 13.4 3 4c0-.6.4-1 1-1h3.5c.6 0 1 .4 1 1 0 1.3.2 2.5.6 3.6.1.3 0 .7-.2 1z"/></svg><span>Phone: 23 456 7890</span></li>
    <li><svg width="14" height="14" viewBox="0 0 24 24"><path fill="#fff" d="M3 5h18v14H3zm2 2v.5l7 5 7-5V7z"/></svg><span>Email:info@company.com</span></li>
  </ul>
  <h4 class="abs foot-h" style="left:912px">Follow Us</h4>
  <div class="abs social"><span aria-label="Social profile 1"></span><span aria-label="Social profile 2"></span><span aria-label="Social profile 3"></span><span aria-label="Social profile 4"></span></div>
  <div class="abs copy">Copyright &copy; 2025&nbsp; All Rights Reserved.</div>
</footer>

</body>
</html>
```